Package Design for Chew Bone Guild for Rivora

Would like a label to put on a 6x9 package.

Here is my site: chewboneguild.example

Here are the labels I like:
https://tomandhound.example/collections/chews/products/6-inch-basic-chews
https://www.rivora.example/stores/Tom+%26+Hound/page/A1D23456-7ABC-42EF-9D01-123456789ABC?ref_=xyz_qrs
https://quiet-meadowland.example/amber-paw-mini-chews-6-25-pack/
https://www.fernandkettle.example/shop/open-trail-chew-rods

```html
<!DOCTYPE html>
<html lang="en">
<head>
<meta charset="utf-8">
<title>Chew Bone Guild – Bully Sticks Label</title>
<link rel="stylesheet" href="https://fonts.googleapis.com/css2?family=Oswald:wght@500&family=Baloo+2:wght@800&display=swap">
<style>
  :root {
    --canvas-bg: #e6e6e6;
    --label-grey-top: #c9cacc;
    --label-grey-bottom: #bfc0c2;
    --ink: #1f1d1e;
    --white: #ffffff;
    --banner-orange: #eda24e;
    --banner-orange-light: #f3b059;
    --banner-red: #bb1d2d;
    --banner-brown: #b4572b;
    --banner-shadow: #1f1d1e;
    --dog-cream: #f1e6d4;
    --dog-tan: #d9aa72;
    --stick-dark: #6b2a1c;
    --stick-mid: #9c4a2a;
    --stick-light: #b86a3c;
  }
  html, body {
    margin: 0;
    padding: 0;
    width: 890px;
    height: 1200px;
    overflow: hidden;
    background: var(--canvas-bg);
  }
  .label {
    position: absolute;
    left: 0;
    top: 64px;
    width: 890px;
    height: 1072px;
    display: block;
  }
  .claim {
    font-family: "Oswald", "Arial Narrow", sans-serif;
    font-weight: 500;
    font-size: 31px;
    fill: var(--ink);
  }
  .band-text {
    font-family: "Oswald", "Arial Narrow", sans-serif;
    font-weight: 500;
    font-size: 54px;
    fill: var(--white);
  }
  .banner-word {
    font-family: "Baloo 2", "Arial Rounded MT Bold", sans-serif;
    font-weight: 800;
    fill: var(--white);
  }
  .brand-name {
    font-family: "Oswald", "Arial Narrow", sans-serif;
    font-weight: 500;
    font-size: 26px;
    fill: var(--ink);
  }
</style>
</head>
<body>
<svg class="label" viewBox="0 0 905 1090" xmlns="http://www.w3.org/2000/svg">
  <defs>
    <linearGradient id="label-bg" x1="0" y1="0" x2="0" y2="1">
      <stop offset="0" stop-color="var(--label-grey-top)"/>
      <stop offset="1" stop-color="var(--label-grey-bottom)"/>
    </linearGradient>
    <radialGradient id="dog-fill" cx="0.5" cy="0.4" r="0.6">
      <stop offset="0" stop-color="var(--dog-cream)"/>
      <stop offset="0.8" stop-color="#e8d7bd"/>
      <stop offset="1" stop-color="var(--dog-tan)" stop-opacity="0"/>
    </radialGradient>
    <linearGradient id="sticks-fill" x1="0" y1="0" x2="1" y2="0">
      <stop offset="0" stop-color="var(--stick-mid)"/>
      <stop offset="0.3" stop-color="var(--stick-light)"/>
      <stop offset="0.55" stop-color="var(--stick-mid)"/>
      <stop offset="0.8" stop-color="var(--stick-light)"/>
      <stop offset="1" stop-color="var(--stick-dark)"/>
    </linearGradient>
  </defs>

  <!-- label ground -->
  <rect class="label-ground" x="0" y="0" width="905" height="830" fill="url(#label-bg)"/>

  <!-- top claims -->
  <g class="claims">
    <text class="claim" x="63" y="63">PREMIUM QUALITY</text>
    <text class="claim" x="63" y="114">GRAS-FED BEEF</text>
    <text class="claim" x="848" y="63" text-anchor="end">IDEAL FOR DENTAL HEALTH</text>
    <text class="claim" x="848" y="114" text-anchor="end">HIGH IN PROTEIN</text>
  </g>

  <!-- dog photo area -->
  <ellipse class="dog-photo" role="img" aria-label="Photo of a smiling yellow Labrador sitting and looking up"
           cx="643" cy="440" rx="195" ry="260" fill="url(#dog-fill)"/>

  <!-- title banners -->
  <g class="title-banners">
    <polygon class="banner-shadow" points="0,260 398,210 388,398 0,405" fill="var(--banner-shadow)"/>
    <polygon class="banner banner-yummy" points="0,258 392,210 383,392 0,398" fill="var(--banner-orange)"/>
    <text class="banner-word" x="48" y="360" font-size="104" transform="rotate(-7 48 360)">yummy</text>

    <polygon class="banner-shadow" points="0,440 350,448 357,622 0,604" fill="var(--banner-shadow)"/>
    <polygon class="banner banner-chew" points="0,437 345,446 350,615 0,598" fill="var(--banner-brown)"/>
    <text class="banner-word" x="50" y="580" font-size="108" transform="rotate(4 50 580)">chew</text>

    <polygon class="banner-shadow" points="128,375 410,336 410,528 128,484" fill="var(--banner-shadow)"/>
    <polygon class="banner banner-dog" points="128,375 404,337 403,520 128,478" fill="var(--banner-red)"/>
    <text class="banner-word" x="198" y="470" font-size="120" transform="rotate(3 198 470)">dog</text>
  </g>

  <!-- product band -->
  <rect class="product-band" x="0" y="715" width="905" height="116" fill="var(--ink)"/>
  <text class="band-text" x="60" y="794">ALL NATURAL</text>
  <text class="band-text" x="852" y="794" text-anchor="end">BULLY STICKS</text>

  <!-- sticks photo area -->
  <rect class="sticks-photo" role="img" aria-label="Close-up photo of dried beef bully sticks laid side by side"
        x="0" y="831" width="905" height="259" fill="url(#sticks-fill)"/>

  <!-- brand seal -->
  <g class="brand-seal">
    <circle cx="453" cy="780" r="113" fill="var(--white)" stroke="var(--ink)" stroke-width="6"/>
    <text class="brand-name" x="453" y="772" text-anchor="middle">CHEW BONE</text>
    <text class="brand-name" x="453" y="806" text-anchor="middle">GUILD</text>
  </g>
</svg>
</body>
</html>
```